****Amazing Solar Energy Company | Needs A Dynamic Website In Wordpress ****

Here at Brivane Solar, our approach is straightforward: we listen, educate, and collaborate. We are a Residential & Commercial solar energy company located in Sanford, FL. OLD TEMP Website https://www.brivanesolar-example.com/

We are looking for a dynamic website design, layout, and code in Wordpress. We will be using a builder (Elementor) post-install so keep that in mind.

IMPORTANT:
Please See brand kit, font type, site map, and even a rough home page. We even have persona targets if needed.

Please review all images and documents uploaded as well

Please rely on your own design with the goal to educate the consumer on the many benefits of solar energy.

Target Market(s)

Home Owners who are looking for Solar Panels

Industry/Entity Type

Solar Energy, Solar Panels, Green Energy

Coding

Coded - Design and coding required

Number of Pages Required

5+ page

Font styles to use
Other font styles liked:
• Header: Raleway Body Text: Montserrat

Colors

Designer to choose colors to be used in the design.

Requirements
Must have
• Must follow the brand kit color, fonts etc | Must be clean and engaging | Modern, Simplistic, Impact, Clean, Cooling, Calming
Nice to have
• Rotating Header, Step By Steps Visuals

```html
<!DOCTYPE html>
<html lang="en">
<head>
<meta charset="utf-8">
<title>Brivane Solar</title>
<link href="https://fonts.googleapis.com/css2?family=Montserrat:wght@400;500;600;700;800&display=swap" rel="stylesheet">
<style>
:root{
  --blue:#0d63c8;
  --blue-deep:#0a4fa6;
  --green:#7ab648;
  --ink:#2d2d2d;
  --muted:#5a5a5a;
  --line:#cfcfcf;
  --stage:#0b0b0b;
  --form:#efefef;
  --white:#ffffff;
}
*{margin:0;padding:0;box-sizing:border-box}
html,body{width:1200px;height:1200px;overflow:hidden;background:var(--stage)}
body{font-family:"Montserrat",sans-serif;color:var(--ink);position:relative}
.page{position:absolute;left:412px;top:0;width:603px;height:1932px;background:var(--white);transform:scale(0.62112);transform-origin:0 0;overflow:hidden}
.abs{position:absolute}
.brand{font-weight:600;color:#1d3b52;letter-spacing:2px;display:flex;align-items:center;gap:5px}
.brand .dot{width:9px;height:9px;border-radius:50%;background:var(--green)}
.nav a{position:absolute;top:19px;font-size:6px;color:var(--ink);text-decoration:none}
.nav a.active{color:var(--blue)}
.social i{position:absolute;top:17px;width:12px;height:12px;border-radius:50%;background:var(--green)}
.call{left:514px;top:15px;font-size:6px;color:var(--green);line-height:9px}
.call b{color:var(--blue);font-weight:600}
.hero-title{left:47px;top:125px;font-size:22px;font-weight:700;color:var(--white);line-height:32px;letter-spacing:.3px}
.hero-text{left:47px;top:191px;width:210px;font-size:6.3px;line-height:12.6px;color:var(--white)}
.btn-ghost{left:47px;top:253px;width:56px;height:18px;border:1px solid var(--white);border-radius:9px;color:var(--white);font-size:6px;font-weight:600;display:flex;align-items:center;justify-content:center}
.btn{height:18px;width:63px;background:var(--blue);color:var(--white);font-size:6px;font-weight:600;display:flex;align-items:center;justify-content:center;box-shadow:0 1px 3px rgba(0,0,0,.25)}
.h2{font-size:19px;font-weight:700;color:var(--blue)}
.body-text{font-size:6px;color:var(--muted)}
.photo{border-radius:2px}
.facility-title{left:0;width:603px;top:677px;text-align:center;color:var(--white);font-size:14.5px;font-weight:700}
.facility-text{left:63px;width:477px;top:703px;text-align:center;color:var(--white);font-size:6px;line-height:12.6px}
.node-label{color:var(--white);font-size:6px;font-weight:600;line-height:8px}
.node-label small{display:block;font-size:3.3px;font-weight:400;line-height:4.6px;width:48px;opacity:.9}
.comments{left:401px;top:1324px;width:156px}
.comments h4{font-size:7.5px;font-weight:500;margin-bottom:6px}
.comments li{list-style:none;font-size:6.3px;height:21.4px;padding-top:6px;border-bottom:1px solid var(--line);display:flex;gap:5px}
.comments li span{color:var(--muted)}
.contact-row{left:92px;display:flex;align-items:center;gap:8px;font-size:6.3px;font-weight:500}
.contact-row .ico{width:25px;height:25px;border-radius:50%;border:1.3px solid var(--green);display:flex;align-items:center;justify-content:center}
.form{left:272px;top:1616px;width:240px;height:170px;background:var(--form)}
.field{position:absolute;background:var(--white);font-size:4.5px;color:var(--muted);padding:6px 9px}
.foot-col h5{font-size:8.5px;font-weight:500;margin-bottom:5px}
.foot-col p{font-size:5.8px;line-height:14px}
.thumb{position:absolute;width:24px;height:22px}
</style>
</head>
<body>
<main class="page">

  <!-- Header -->
  <header>
    <div class="abs brand" style="left:48px;top:16px;font-size:11px">BRIVANE <span class="dot"></span></div>
    <nav class="nav">
      <a class="active" style="left:186px">Home</a>
      <a style="left:221px">About Us</a>
      <a style="left:266px">Service</a>
      <a style="left:306px">Blogs</a>
      <a style="left:339px">Contact Us</a>
    </nav>
    <div class="social">
      <i style="left:436px"></i><i style="left:453px"></i><i style="left:469px"></i><i style="left:485px"></i>
    </div>
    <div class="abs call">Call Us Today<br><b>+123 555 0142</b></div>
  </header>

  <!-- Hero -->
  <section class="hero">
    <svg class="abs" style="left:0;top:47px" width="603" height="305" viewBox="0 0 603 305">
      <defs>
        <linearGradient id="heroSky" x1="0" y1="0" x2="1" y2="1">
          <stop offset="0" stop-color="#3d6fb0"/>
          <stop offset=".55" stop-color="#274c86"/>
          <stop offset="1" stop-color="#1b3766"/>
        </linearGradient>
      </defs>
      <path d="M0 265 L160 302 L603 258 L603 0 L0 0 Z" fill="url(#heroSky)" role="img" aria-label="Technician installing solar panels on a rooftop"/>
      <path d="M0 265 L160 302 L120 302 L0 277 Z" fill="var(--blue)"/>
    </svg>
    <h1 class="abs hero-title">CLEARLY ENERGY<br>DATA INSIGHTS</h1>
    <p class="abs hero-text">Solar energy is radiant light and heat from the Sun that is harnessed using a range of technologies such as solar power to generate electricity, solar thermal energy including solar water heating, and solar architecture.[1][2]</p>
    <div class="abs btn-ghost">Get Started</div>
    <svg class="abs" style="left:282px;top:312px" width="40" height="10">
      <circle cx="5" cy="5" r="3.6" fill="#fff"/><circle cx="14" cy="5" r="3.6" fill="#fff"/><circle cx="23" cy="5" r="3.6" fill="#fff"/><circle cx="32" cy="5" r="3.6" fill="#fff"/>
    </svg>
  </section>

  <!-- Divider -->
  <svg class="abs" style="left:0;top:368px" width="603" height="24">
    <line x1="0" y1="11.5" x2="278" y2="11.5" stroke="var(--blue-deep)" stroke-width="1"/>
    <line x1="324" y1="11.5" x2="603" y2="11.5" stroke="var(--blue-deep)" stroke-width="1"/>
    <circle cx="301" cy="11.5" r="10.5" fill="var(--blue)"/>
    <path d="M297 10 L301 14 L305 10" fill="none" stroke="#fff" stroke-width="1.5"/>
  </svg>

  <!-- About -->
  <section class="about">
    <div class="abs photo" role="img" aria-label="Power transmission tower at sunset above solar panels" style="left:0;top:410px;width:305px;height:220px;background:linear-gradient(180deg,#4f5660 0%,#a08a6a 45%,#e7b25a 62%,#3d3b38 80%,#222 100%)"></div>
    <h2 class="abs h2" style="left:324px;top:418px">About Us</h2>
    <p class="abs body-text" style="left:324px;top:451px;width:236px;line-height:14.2px;font-size:6.2px">Solar energy is radiant light and heat from the Sun that is harnessed using a range of technologies such as solar power to generate electricity, solar thermal energy including solar water heating, and solar architecture.[1][2]It is an essential source of renewable energy, and its technologies are broadly characterized as either passive solar or active solar depending on how they capture and distribute solar energy or convert it into solar power. Active solar techniques include the use of photovoltaic systems, concentrated solar power, and solar water heating to harness the energy. Passive solar techniques include orienting a building to the Sun, selecting materials with favorable thermal mass or</p>
    <div class="abs btn" style="left:324px;top:602px">Learn More</div>
  </section>

  <!-- Facility -->
  <section class="facility">
    <svg class="abs" style="left:0;top:649px" width="603" height="390" viewBox="0 0 603 390">
      <path d="M0 0 H603 V326 L440 386 L0 338 Z" fill="var(--blue)"/>
      <path d="M603 326 L603 346 L448 386 L440 386 Z" fill="var(--green)"/>
      <g fill="none" stroke="#fff" stroke-width="2.5">
        <path d="M158 136 H206 V183"/>
        <path d="M138 220 H185"/>
        <path d="M144 306 H192 V282"/>
        <path d="M435 136 H384 V183"/>
        <path d="M454 220 H404"/>
        <path d="M448 306 H398 V282"/>
        <circle cx="294" cy="234" r="109"/>
      </g>
      <circle cx="294" cy="234" r="90" fill="#fff"/>
      <circle cx="294" cy="234" r="66" fill="#dfeaf7" role="img" aria-label="Solar panel with sun and green leaves"/>
      <g fill="#fff">
        <circle cx="142" cy="136" r="16"/><circle cx="122" cy="220" r="16"/><circle cx="128" cy="306" r="16"/>
        <circle cx="451" cy="136" r="16"/><circle cx="470" cy="220" r="16"/><circle cx="464" cy="306" r="16"/>
      </g>
      <g fill="none" stroke="var(--green)" stroke-width="1.2">
        <rect x="135" y="131" width="14" height="9"/><line x1="142" y1="131" x2="142" y2="140"/>
        <rect x="117" y="214" width="10" height="12" rx="2"/>
        <circle cx="128" cy="306" r="6"/>
        <path d="M444 141 L451 131 L458 141 Z"/>
        <path d="M465 215 L470 213 L475 215 V221 Q470 226 465 221 Z" fill="var(--green)"/>
        <rect x="456" y="302" width="14" height="8" rx="1"/>
      </g>
      <path d="M467 220 L469.5 222 L473 218" fill="none" stroke="#fff" stroke-width="1.2"/>
    </svg>
    <h2 class="abs facility-title">MODERN FACILITY-MANAGEMENT AND MANUFACTURING</h2>
    <p class="abs facility-text">The Earth receives 174 petawatts (PW) of incoming solar radiation (insolation) at the upper atmosphere.[5] Approximately 30% is reflected back to space while the rest is absorbed by clouds, oceans and land masses. The spectrum of solar light at the Earth's surface is mostly spread across the visible and near-infrared ranges with a small part in the near-ultraviolet.[6] Most of the world's population live in areas with insolation levels of 150–300 watts/m2, or 3.5–7.0 kWh/m2 per day.[7]</p>
    <div class="abs node-label" style="left:75px;top:773px">Solar Panel<small>Panel output depends on roof angle and daily sun.</small></div>
    <div class="abs node-label" style="left:50px;top:858px">Solar Panel Cost<small>Costs vary with system size and local rates.</small></div>
    <div class="abs node-label" style="left:58px;top:944px">Solar Financing<small>Flexible plans make going solar simple and affordable.</small></div>
    <div class="abs node-label" style="left:471px;top:774px">Solar Pros &amp; Cons<small>Weigh savings and upkeep before you choose.</small></div>
    <div class="abs node-label" style="left:490px;top:859px">Solar Rebates<small>Local programs can lower your upfront system cost.</small></div>
    <div class="abs node-label" style="left:484px;top:944px">Solar Battery<small>Store extra daytime power for use at night.</small></div>
  </section>

  <!-- Goals -->
  <section class="goals">
    <svg class="abs" style="left:56px;top:1055px" width="160" height="126"><path d="M0 0 H157 V9 H11 V125 H0 Z" fill="var(--green)"/></svg>
    <div class="abs photo" role="img" aria-label="Team of solar company staff in matching blue shirts standing outdoors" style="left:67px;top:1064px;width:229px;height:181px;background:linear-gradient(180deg,#b8c9d8 0%,#8f8676 40%,#2f4f7e 70%,#3a4a66 100%)"></div>
    <h2 class="abs h2" style="left:312px;top:1063px">Your Company Goals</h2>
    <p class="abs body-text" style="left:311px;top:1093px;width:240px;line-height:12.6px">Solar radiation is absorbed by the Earth's land surface, oceans – which cover about 71% of the globe – and atmosphere. Warm air containing evaporated water from the oceans rises, causing atmospheric circulation or convection. When the air reaches a high altitude, where the temperature is low, water vapor condenses into clouds, which rain onto the Earth's surface, completing the water cycle. The latent heat of water condensation amplifies convection, producing atmospheric phenomena such as wind, cyclones and anticyclones.[8] Sunlight absorbed by the oceans and land masses keeps the surface at an average temperature of 14 °C.[9] By photosynthesis, green plants convert solar energy into chemically</p>
    <div class="abs btn" style="left:311px;top:1228px">Learn More</div>
  </section>

  <!-- Blogs -->
  <section class="blogs">
    <h2 class="abs h2" style="left:0;width:603px;text-align:center;top:1272px">Our Blogs</h2>
    <div class="abs" role="img" aria-label="Ground-mounted solar panel array under a blue sky" style="left:47px;top:1311px;width:343px;height:185px;background:linear-gradient(180deg,#2f7fd0 0%,#7db8e8 45%,#1f3f8c 62%,#4d8a3a 80%,#3f7a2e 100%)"></div>
    <svg class="abs" style="left:55px;top:1395px" width="330" height="18">
      <path d="M10 2 L3 9 L10 16" fill="none" stroke="#fff" stroke-width="2"/>
      <path d="M318 2 L325 9 L318 16" fill="none" stroke="#fff" stroke-width="2"/>
    </svg>
    <ul class="abs comments">
      <h4>Recent Comment</h4>
      <li>›<span>Alex Moor on Classic Shoes men.</span></li>
      <li>›<span>Alex Moor on Classic Shoes men.</span></li>
      <li>›<span>Alex Moor on Classic Shoes men.</span></li>
      <li>›<span>Alex Moor on Classic Shoes men.</span></li>
      <li>›<span>Alex Moor on Classic Shoes men.</span></li>
      <li>›<span>Alex Moor on Classic Shoes men.</span></li>
      <li>›<span>Alex Moor on Classic Shoes men.</span></li>
    </ul>
    <div class="abs" style="left:47px;top:1503px;font-size:14px;font-weight:600;color:#8a8a8a">10</div>
    <div class="abs" style="left:47px;top:1521px;font-size:8.5px;font-weight:600">Apr</div>
    <h3 class="abs" style="left:74px;top:1502px;font-size:15.5px;font-weight:700;color:var(--blue)">Solar Energy House Panel</h3>
    <div class="abs" style="left:74px;top:1525px;font-size:4px;color:#8a8a8a;display:flex;gap:16px"><span>▪ 0 Message</span><span>▪ 12 like</span><span>▪ 20 Blogs</span></div>
    <p class="abs body-text" style="left:74px;top:1537px;width:235px;line-height:12.6px">Active solar techniques use photovoltaics, concentrated solar power, solar thermal collectors, pumps, and fans to convert sunlight into useful outputs. Passive solar techniques include selecting materials with</p>
    <div class="abs btn" style="left:74px;top:1579px">Learn More</div>
  </section>

  <!-- Contact -->
  <section class="contact">
    <h2 class="abs h2" style="left:92px;top:1616px">Get In Touch</h2>
    <div class="abs contact-row" style="top:1655px"><span class="ico"><svg width="10" height="12"><path d="M5 11 C1 6 1 4 1 4 A4 4 0 0 1 9 4 C9 4 9 6 5 11Z" fill="var(--green)"/><circle cx="5" cy="4" r="1.5" fill="#fff"/></svg></span>Harbor lane block-410 512/</div>
    <div class="abs contact-row" style="top:1696px"><span class="ico"><svg width="12" height="12"><circle cx="6" cy="6" r="6" fill="var(--green)"/><path d="M3.5 3.5 Q3.5 8.5 8.5 8.5 L8.5 7 L7 6.5 L6.3 7.2 Q4.8 6.5 4.8 5.2 L5.5 4.5 L5 3Z" fill="#fff"/></svg></span>+ 0321-555-014</div>
    <div class="abs contact-row" style="top:1737px"><span class="ico"><svg width="12" height="9"><rect width="12" height="9" rx="1" fill="var(--green)"/><path d="M0.5 1 L6 5 L11.5 1" fill="none" stroke="#fff" stroke-width="1"/></svg></span>www. Brivane Solar Panel. com</div>
    <form class="abs form">
      <div class="field" style="left:21px;top:12px;width:94px;height:18px">First Name</div>
      <div class="field" style="left:125px;top:12px;width:94px;height:18px">Last Name</div>
      <div class="field" style="left:21px;top:40px;width:94px;height:18px">Email Address</div>
      <div class="field" style="left:125px;top:40px;width:94px;height:18px">Password</div>
      <div class="field" style="left:21px;top:68px;width:198px;height:66px">Message</div>
      <div class="abs btn" style="left:156px;top:141px">Learn More</div>
    </form>
  </section>

  <!-- Footer -->
  <footer>
    <div class="abs brand" style="left:47px;top:1838px;font-size:14px">BRIVANE <span class="dot"></span></div>
    <p class="abs body-text" style="left:47px;top:1870px;width:110px;line-height:12.4px">Besides, land availability has a large effect on the available solar energy because solar panels can</p>
    <div class="abs foot-col" style="left:185px;top:1827px"><h5>Quick Links</h5><p>Home<br>About<br>Service<br>Blog<br>Contact Us</p></div>
    <div class="abs foot-col" style="left:267px;top:1827px"><h5>Contact Us</h5><p>Address Main 88 Larkin<br>Street West Orchard 014<br>+ 1258 555 031<br>+125 555 208 417<br>www.Brivane Solar Panel.com</p></div>
    <div class="abs foot-col" style="left:391px;top:1827px"><h5>Social Links</h5><p>Facenote<br>Chirper<br>Snapgram<br>ViewTube<br>Chatcord</p></div>
    <div class="abs foot-col" style="left:473px;top:1827px"><h5>Recent Works</h5></div>
    <div role="img" aria-label="Recent solar project photos">
      <span class="thumb" style="left:473px;top:1846px;background:linear-gradient(#6d7a8a,#e0a050)"></span>
      <span class="thumb" style="left:503px;top:1846px;background:linear-gradient(#4a5a3a,#c79a40)"></span>
      <span class="thumb" style="left:532px;top:1846px;background:linear-gradient(#3f7fd0,#5a9a3a)"></span>
      <span class="thumb" style="left:473px;top:1875px;background:linear-gradient(#7fb4e6,#2a4f9a)"></span>
      <span class="thumb" style="left:503px;top:1875px;background:linear-gradient(#4a6aa0,#1e3a7a)"></span>
      <span class="thumb" style="left:532px;top:1875px;background:linear-gradient(#c08060,#3a4f8a)"></span>
    </div>
    <p class="abs" style="left:0;width:603px;text-align:center;top:1920px;font-size:4.5px;color:var(--muted)">CopyRight by Brivane Solar, All Right Reserved.</p>
  </footer>

</main>
</body>
</html>
```